Bulldog themed background for Real Estate Purchase Letter

I need a phantom background or watermark on a standard 8 1/2" x 11" paper. I am going to put a letter over the background. I want a bulldog theme that is cute, funny and original. This letter is for a real estate project and we want to capture the person sub-consciously . Attached is my personal dogs. If you want to use them you can but not required. I have attached the letter that I am trying to emulate. I want bulldogs not horses.

Target Market(s)

45 years old and higher

Industry/Entity Type

Real Estate

Font styles to use
Serif
Sans Serif

Colors

Designer to choose colors to be used in the design.

Requirements
Must have
• fun, happiness, reassuring,
Should not have
• violence, negativity, unhappy

```html
<!DOCTYPE html>
<html lang="en">
<head>
<meta charset="utf-8">
<title>Purchase Letter</title>
<link rel="stylesheet" href="https://fonts.googleapis.com/css2?family=Open+Sans:wght@300;400;600&family=Montserrat:wght@500&display=swap">
<style>
  :root {
    --brand-deep: #0a4fb8;
    --brand-mid: #0f6fd6;
    --brand-sky: #17b3ee;
    --mascot-tint: #c9d4e0;
    --ink: #3a3a3a;
    --paper: #ffffff;
  }
  * { margin: 0; padding: 0; box-sizing: border-box; }
  html, body { width: 850px; height: 1200px; overflow: hidden; background: var(--paper); }
  .letterhead {
    position: relative;
    width: 850px;
    height: 1200px;
    overflow: hidden;
    background: var(--paper);
    font-family: "Open Sans", Arial, sans-serif;
    font-weight: 300;
    color: var(--ink);
  }
  .wave, .mascot-watermark { position: absolute; left: 0; top: 0; }
  .agent-id {
    position: absolute;
    left: 67px;
    top: 48px;
    font-family: "Montserrat", Arial, sans-serif;
    font-weight: 500;
    font-size: 18px;
    line-height: 25px;
    color: var(--paper);
    letter-spacing: 0.3px;
  }
  .letter {
    position: absolute;
    left: 69px;
    top: 198px;
    width: 711px;
    font-size: 18.4px;
    line-height: 30px;
  }
  .strong { font-weight: 400; }
  .recipient { margin-bottom: 44px; }
  .salutation { margin-bottom: 39px; }
  .body-copy p {
    text-align: justify;
    text-indent: 39px;
    line-height: 32.7px;
    margin-bottom: 36px;
  }
  .sign-off { margin-top: 46px; }
  .signature { margin-top: 42px; font-weight: 400; }
</style>
</head>
<body>
<main class="letterhead">
  <svg class="mascot-watermark" width="850" height="1200" viewBox="0 0 850 1200" role="img" aria-label="Large faint bulldog mascot watermark behind the letter">
    <defs>
      <radialGradient id="mascotGlow" cx="0.5" cy="0.45" r="0.6">
        <stop offset="0" stop-color="var(--mascot-tint)" stop-opacity="0.55"/>
        <stop offset="1" stop-color="var(--mascot-tint)" stop-opacity="0.25"/>
      </radialGradient>
    </defs>
    <path d="M150 330 C150 210 260 150 400 145 C560 140 680 210 710 330 C760 430 850 520 850 640 L850 900 C760 980 600 1050 420 1080 C300 1095 120 1040 80 960 C60 800 90 620 120 500 C130 440 150 390 150 330 Z" fill="url(#mascotGlow)"/>
  </svg>

  <svg class="wave wave-top" width="850" height="260" viewBox="0 0 850 260" aria-hidden="true">
    <path d="M0 0 H560 C470 60 330 95 200 125 C100 148 40 175 0 240 Z" fill="var(--brand-sky)"/>
    <path d="M0 0 H545 C450 55 320 88 195 113 C95 135 35 160 0 220 Z" fill="var(--brand-mid)"/>
    <path d="M0 0 H420 C330 45 220 70 120 90 C60 102 20 120 0 140 Z" fill="var(--brand-deep)"/>
  </svg>

  <svg class="wave wave-bottom" width="850" height="1200" viewBox="0 0 850 1200" aria-hidden="true">
    <path d="M850 935 C780 975 690 995 560 1035 C430 1080 330 1140 195 1200 H850 Z" fill="var(--brand-sky)"/>
    <path d="M850 955 C780 990 690 1010 565 1050 C440 1092 340 1150 212 1200 H850 Z" fill="var(--brand-mid)"/>
    <path d="M850 1040 C760 1075 640 1110 520 1150 C470 1168 430 1185 395 1200 H850 Z" fill="var(--brand-deep)"/>
  </svg>

  <div class="agent-id">Real Estate Agent ID :<br>#0198273645</div>

  <article class="letter">
    <address class="recipient" style="font-style:normal">
      <div class="strong">Mr. Outta Stateowner</div>
      <div>123456 Main Street</div>
      <div>Ocala FL 3440-5360</div>
    </address>

    <p class="salutation">Dear <span class="strong">First Name</span></p>

    <section class="body-copy">
      <p>I am writing you, because I am interested in purchasing your property located at <span class="strong">123456 Main Street Ocala FL 3440-5360</span> I live nearby in Morriston and I puschages properties throught the state of PA Currently I am working on projects in the neighbourhood, which is how I learned of your property.</p>
      <p>Please call me at <span class="strong">(XXX) XXXX-Local#</span> so I can tell you how we can buy your property quickly, with no hassels and most importantly, at a fair price. I purchase the hous directly from you so there are no real estate commissions or extra fees coming out of your pocket. Furthermore, I always make cash offers so you never have to worry about delays resulting from a buyer trying to qualify for a mortgage and wasting your valuable time.</p>
      <p>I'will be glade to personally tell you more about how we can work together. All call are completely confidential and there is no obligation whatsoever. Even if you are not intersted in selling at thing time call <span class="strong">(xxx) xxxx-xxxx</span>, so I can help you with determining the value of your property. You should also keep this letter for your future reference, since things in life have a tendency to change unexpectedly. Thanks you for your time and consideration and I look forward to speaking with you.</p>
    </section>

    <p class="sign-off">Sincerely,</p>
    <p class="signature">Dana Whitfield</p>
  </article>
</main>
</body>
</html>
```